New Business Card Design Project

I would like a business card to match my truck wrap and logo. I would like the font to match my existing business card please.

Industry/Entity Type

Painter

Contact Information for Business Card

Rodrigo Venter 801-437-2910 Ventercoatings.utah@brushmail.net
SERVICES - Custom Paint & Stain, Interior & Exterior, Epoxy Coatings / Garage Floors, Cabinet Refinishing, Log Staining and Refinishing.

Requirements
Nice to have
• I would like to have the white and grey line like the bottom of my vehicle wrap, Light Grey to match my truck also.

```html
<!DOCTYPE html>
<html lang="en">
<head>
<meta charset="utf-8">
<title>Venter Painting – Business Card</title>
<link href="https://fonts.googleapis.com/css2?family=Arimo:wght@400;700&display=swap" rel="stylesheet">
<style>
  :root {
    --page-bg: #2b2b2d;
    --blue-deep: #1a5fa3;
    --blue-mid: #1f7fc4;
    --blue-bright: #2aa6e0;
    --grey-light: #b9bcc3;
    --grey-mid: #9a9ea7;
    --white: #ffffff;
    --text-grey: #7d8189;
  }
  * { margin: 0; padding: 0; box-sizing: border-box; }
  html, body { width: 1200px; height: 900px; overflow: hidden; }
  body {
    background: var(--page-bg);
    font-family: "Arimo", Arial, sans-serif;
    position: relative;
  }
  .card {
    position: absolute;
    left: 250px;
    width: 700px;
    height: 400px;
    border-radius: 26px;
    overflow: hidden;
  }
  .card-front { top: 40px; background: var(--white); }
  .card-back { top: 460px; background: var(--grey-light); }
  .card-shapes { position: absolute; inset: 0; }

  .brand {
    position: absolute;
    display: flex;
    align-items: center;
    gap: 16px;
    font-weight: 700;
    letter-spacing: 2px;
  }
  .brand-mark { width: 44px; height: 44px; border-radius: 6px; flex: none; }
  .card-front .brand { left: 150px; top: 70px; color: var(--blue-mid); font-size: 40px; }
  .card-front .brand-mark { background: var(--blue-mid); }
  .card-back .brand {
    left: 40px; top: 100px;
    color: var(--white);
    font-size: 30px;
    line-height: 1.1;
  }
  .card-back .brand-mark { background: var(--white); }

  .front-services {
    position: absolute;
    left: 40px; right: 40px; top: 190px;
    text-align: center;
  }
  .services-title {
    font-weight: 700;
    font-size: 24px;
    letter-spacing: 1px;
  }
  .front-services .services-title { color: var(--blue-mid); margin-bottom: 12px; }
  .front-services p {
    color: var(--text-grey);
    font-size: 17px;
    line-height: 1.6;
  }
  .dot { color: var(--blue-mid); padding: 0 4px; }

  .back-services {
    position: absolute;
    right: 30px; top: 36px;
    text-align: right;
    color: var(--white);
  }
  .back-services .services-title { font-size: 26px; margin-bottom: 6px; }
  .back-services ul { list-style: none; }
  .back-services li { font-size: 18px; line-height: 1.4; }
  .back-services li::after {
    content: "";
    display: inline-block;
    width: 8px; height: 8px;
    border-radius: 50%;
    background: var(--white);
    margin-left: 8px;
    vertical-align: middle;
  }
  .contact {
    position: absolute;
    right: 30px; top: 262px;
    text-align: right;
    color: var(--white);
    font-size: 16px;
    line-height: 1.9;
  }
  .contact-line { display: flex; align-items: center; justify-content: flex-end; gap: 10px; }
  .contact-line svg { width: 17px; height: 17px; }
  .person-name {
    position: absolute;
    left: 40px; top: 290px;
    color: var(--white);
    font-weight: 700;
    font-size: 26px;
    letter-spacing: 1px;
    text-transform: uppercase;
  }
</style>
</head>
<body>

<section class="card card-front">
  <svg class="card-shapes" viewBox="0 0 700 400" preserveAspectRatio="none">
    <defs>
      <linearGradient id="frontBand" x1="0" y1="1" x2="1" y2="0">
        <stop offset="0" stop-color="#2aa6e0"/>
        <stop offset="1" stop-color="#1a5fa3"/>
      </linearGradient>
    </defs>
    <path d="M0,360 L190,360 L215,345 L580,345 L615,300 L700,300 L700,400 L0,400 Z" fill="url(#frontBand)"/>
    <path d="M0,352 L186,352 L211,337 L576,337 L611,292 L700,292" fill="none" stroke="#b9bcc3" stroke-width="3"/>
  </svg>
  <div class="brand"><span class="brand-mark"></span>VENTER PAINTING</div>
  <div class="front-services">
    <div class="services-title">SERVICES</div>
    <p><span class="dot">•</span>Custom Paint &amp; Stain <span class="dot">•</span>Interior &amp; Exterior <span class="dot">•</span>Epoxy Coatings / Garage Floors<br>
    <span class="dot">•</span>Cabinet Refinishing <span class="dot">•</span>Log Staining and Refinishing.</p>
  </div>
</section>

<section class="card card-back">
  <svg class="card-shapes" viewBox="0 0 700 400" preserveAspectRatio="none">
    <defs>
      <linearGradient id="backBlue" x1="0" y1="1" x2="1" y2="0">
        <stop offset="0" stop-color="#1a5fa3"/>
        <stop offset="0.55" stop-color="#1f7fc4"/>
        <stop offset="1" stop-color="#2aa6e0"/>
      </linearGradient>
    </defs>
    <path d="M0,0 L700,0 L700,232 L400,232 L360,345 L0,345 Z" fill="url(#backBlue)"/>
    <path d="M700,240 L406,240 L366,353 L0,353" fill="none" stroke="#1f7fc4" stroke-width="4"/>
  </svg>
  <div class="brand"><span class="brand-mark"></span><span>VENTER<br>PAINTING</span></div>
  <div class="back-services">
    <div class="services-title">SERVICES</div>
    <ul>
      <li>Custom Paint &amp; Stain</li>
      <li>Interior &amp; Exterior</li>
      <li>Epoxy Coatings / Garage Floors</li>
      <li>Cabinet Refinishing</li>
      <li>Log Staining and Refinishing</li>
    </ul>
  </div>
  <div class="contact">
    <div class="contact-line">801-437-2910
      <svg viewBox="0 0 24 24" fill="none" stroke="#fff" stroke-width="2"><path d="M5 3h4l2 5-2.5 1.5a11 11 0 0 0 6 6L16 13l5 2v4a2 2 0 0 1-2 2A16 16 0 0 1 3 5a2 2 0 0 1 2-2z"/></svg>
    </div>
    <div class="contact-line">Ventercoatings.utah@brushmail.net
      <svg viewBox="0 0 24 24" fill="none" stroke="#fff" stroke-width="2"><rect x="3" y="5" width="18" height="14" rx="1"/><path d="M3 6l9 7 9-7"/></svg>
    </div>
  </div>
  <div class="person-name">Rodrigo Venter</div>
</section>

</body>
</html>
```